Exclusive British Dental Clinic Needs Modern Brochure to Attract New Patients

We are looking to create a smart, sophisticated brochure that gives the public and future potential clients a concise overview of what we offer and why the quality and care on offer is a step above the rest. We are based in the United Kingdom where the Public Wellness Board provide dental care free or at low cost. We are NOT an PWB provider. We are a wholly private dental clinic so all of our patients are paying full-price premium prices directly out of pocket. The work we do is exceptional so all of our patients can be assured that anything we do is done to the highest and best quality possible.
We offer high quality dental treatment using the best and latest techniques, materials and an award winning dental laboratory. All treatments are undertaken using high quality magnification to ensure the best possible result. We have over 30 years’ experience in general dentistry with fully trained staff. In quality comfortable surroundings, we are a caring practice with excellent patient care. We allow more time with our patients and we understand and care for nervous patients.
We also offer facial fillers, wrinkle reducers and teeth whitening in order to help our patients achieve their best look.

We have attached our logo and logo icons to this brief.
We also have attached some information in our Brochure Details document. This just highlights what we would like to see and more information about us.
We are really up to suggestion with design and wording because we want this brochure to be attractive and appealing to the public.
Feel free to edit as you see fit to help us attain our goals :)

Reason: Hello We are very excited about the work we have received thus far...our Practice Manager is away for the next week and we wanted to make sure we are all on board for the discussions and decisions we make moving forward. Thank you for taking the time to help us create our voice! --- Larkmoor Atelier Dental Clinic

```html
<!DOCTYPE html>
<html lang="en">
<head>
<meta charset="utf-8">
<title>Larkmoor Atelier Dental Clinic – Brochure Inside</title>
<link rel="stylesheet" href="https://fonts.googleapis.com/css2?family=Open+Sans:ital,wght@0,300;0,400;0,700;1,400&display=swap">
<style>
  :root {
    --stage: #3b3b3d;
    --paper: #ffffff;
    --ink: #4a4a4c;
    --brand-blue: #7fa6d6;
    --brand-navy: #2c4a7c;
    --rule: #9fbde0;
    --divider: #e2e2e4;
    --row-dark: #dcdcdf;
    --row-light: #efeff1;
    --label: #d8d8da;
  }
  * { box-sizing: border-box; margin: 0; padding: 0; }
  html, body { width: 1200px; height: 900px; overflow: hidden; }
  body {
    background: var(--stage);
    font-family: "Open Sans", Arial, sans-serif;
    color: var(--ink);
    position: relative;
  }
  .brochure {
    position: absolute;
    left: 44px; top: 57px;
    width: 1112px; height: 786px;
    background: var(--paper);
  }
  .panel {
    position: absolute; top: 0; height: 786px;
  }
  .panel--intro { left: 0; width: 370px; }
  .panel--services { left: 370px; width: 371px; border-left: 1px solid var(--divider); }
  .panel--faq { left: 741px; width: 371px; border-left: 1px solid var(--divider); }

  /* Intro panel */
  .brand {
    position: absolute; left: 76px; top: 224px;
    display: flex; align-items: center; gap: 12px;
  }
  .brand__mark {
    width: 14px; height: 14px; border-radius: 50%;
    background: var(--brand-blue);
  }
  .brand__name {
    font-size: 15px; font-weight: 400; letter-spacing: 0.6px;
    color: var(--brand-navy); text-transform: uppercase; line-height: 19px;
  }
  .intro-text {
    position: absolute; left: 50px; top: 326px; width: 270px;
    text-align: center; font-size: 13px; line-height: 25px; color: var(--ink);
  }

  /* Section headings */
  .section-title {
    position: absolute; left: 30px; width: 310px;
    border-top: 2px dotted var(--rule);
    border-bottom: 2px dotted var(--rule);
    padding: 4px 0 3px;
    font-size: 16px; font-weight: 300; color: var(--brand-blue);
    letter-spacing: 0.3px; text-transform: uppercase; line-height: 19px;
  }
  .panel--services .section-title--services { top: 47px; }
  .panel--services .section-title--prices { top: 361px; }
  .panel--faq .section-title { left: 30px; width: 312px; top: 47px; }

  /* Services */
  .services-lead {
    position: absolute; left: 30px; top: 94px; width: 320px;
    font-size: 13px; line-height: 19.6px;
  }
  .services-list-title {
    position: absolute; left: 30px; top: 173px;
    font-size: 13px; line-height: 19.6px;
  }
  .services-list {
    position: absolute; left: 30px; top: 192px;
    list-style: none; font-size: 13px; line-height: 19.6px;
  }
  .services-list li::before { content: "•"; margin-right: 7px; }

  /* Prices table */
  .price-table {
    position: absolute; left: 30px; top: 408px; width: 311px;
    border-collapse: separate; border-spacing: 0 1px;
    font-size: 13px;
  }
  .price-table td { padding: 0 12px; height: 25.5px; }
  .price-table tr:nth-child(odd) td { background: var(--row-dark); }
  .price-table tr:nth-child(even) td { background: var(--row-light); }
  .price-table td.price { text-align: center; width: 127px; border-left: 2px solid var(--paper); }
  .price-table tr.tall td { height: 40px; line-height: 14px; }
  .footnote {
    position: absolute; left: 30px; top: 726px; width: 290px;
    font-size: 9.5px; font-style: italic; line-height: 12px; color: #6a6a6c;
  }
  .footnote span { display: block; padding-left: 10px; text-indent: -10px; }

  /* FAQ */
  .faq {
    position: absolute; left: 30px; top: 95px; width: 314px;
  }
  .faq__q {
    font-size: 11px; font-weight: 700; color: var(--brand-blue);
    line-height: 15.4px;
  }
  .faq__a {
    font-size: 11px; line-height: 15.4px; margin-bottom: 6px;
  }

  .view-label {
    position: absolute; right: 44px; top: 861px;
    font-size: 16px; font-weight: 300; color: var(--label);
  }
</style>
</head>
<body>
  <main class="brochure">
    <section class="panel panel--intro">
      <div class="brand">
        <span class="brand__mark"></span>
        <span class="brand__name">Larkmoor Atelier<br>Dental Clinic</span>
      </div>
      <p class="intro-text">Larkmoor Atelier Dental Clinic is a welcoming, modern facility where we offer the highest quality treatment.&nbsp; Through our treatment approach, we aim to improve each patient’s health and well being—for us that means we will work with our patients to make their visit a positive one by creating a treatment plan that works for them and what they want to accomplish.</p>
    </section>

    <section class="panel panel--services">
      <h2 class="section-title section-title--services">Our Services</h2>
      <p class="services-lead">We offer a full range of treatment options in cosmetic dentistry and facial cosmetic rejuvenation. Looking good often translates into feeling good.</p>
      <p class="services-list-title">Treatments Include:</p>
      <ul class="services-list">
        <li>Whitening</li>
        <li>Veneers</li>
        <li>Tooth Coloured Fillings</li>
        <li>Crowns</li>
        <li>Wrinkle Reducers</li>
        <li>Facial Fillers</li>
        <li>Lip Enhancement</li>
      </ul>

      <h2 class="section-title section-title--prices">Treatment Prices</h2>
      <table class="price-table">
        <tr class="tall"><td>New Patient Examination and Consultation</td><td class="price">£150.00</td></tr>
        <tr><td>Routine Examination</td><td class="price">£70.00</td></tr>
        <tr><td>Hygienist Visit</td><td class="price">From £75.00</td></tr>
        <tr><td>Fillings</td><td class="price">From £150.00</td></tr>
        <tr><td>Veneers</td><td class="price">From £725.00</td></tr>
        <tr><td>Crowns</td><td class="price">From £775.00</td></tr>
        <tr><td>Whitening</td><td class="price">From £399.00</td></tr>
        <tr><td>Wrinkle Reducers</td><td class="price">From £225.00</td></tr>
        <tr><td>Facial Fillers</td><td class="price">From £275.00</td></tr>
        <tr><td>Lip Enhancement</td><td class="price">From £295.00</td></tr>
      </table>
      <p class="footnote"><span>*&nbsp; All treatments are carried out under optical magnification systems for improved accuracy. We are a mercury free practice*</span></p>
    </section>

    <section class="panel panel--faq">
      <h2 class="section-title">FAQs</h2>
      <div class="faq">
        <p class="faq__q">What is involved in an initial consultation?</p>
        <p class="faq__a">We believe this is the most important appointment. Each patient is an individual and An initial consultation consists of a full examination of all hard and soft tissue, an oral cancer screening, and periodontal examination as well as any necessary radiographs, photographs and/or special tests.</p>
        <p class="faq__q">How often should I see the dentist?</p>
        <p class="faq__a">We recommend a six-monthly visit to both the dentist and hygienist to keep your teeth in optimum health. Research shows that a visit to the dentist every 6 months will help to prevent gum disease, cavities and the need for extensive dental treatment.</p>
        <p class="faq__q">Why should I choose private dental care?</p>
        <p class="faq__a">Private treatment offers a broad range of general and cosmetic dentistry with the aim of creating a smile you are happy with, attractive confident. waiting time is considerably less, but our attention to detail and time spent on each appointment is greater as we are not worried about targets so we can give you more attention and time during treatment. range of treatment</p>
        <p class="faq__q">What happens during a scale and polish?</p>
        <p class="faq__a">Think of a ‘scale’ as a powerwash for your teeth. Brushing can only get rid of surface plaque but scaling gets rid of hard formed tartar; Polishing helps to remove surface staining.</p>
        <p class="faq__q">Is teeth whitening safe?</p>
        <p class="faq__a">Yes. Clinical studies have shown that whitening your teeth with carbamide or hydrogen peroxide under the supervision of a dental professional is safe for teeth and gums.&nbsp; All of our whitening options are EU compliant</p>
        <p class="faq__q">What are facial fillers and will they correct my wrinkles?</p>
        <p class="faq__a">Facial fillers are compromised of injectable hyaluronic acid, which can hold 2000 times its weight in moisture. They improve the appearance of fine lines and wrinkles, but may not completely correct. Each experience varies by individual. We offer a complete consultation prior to carrying out treatment where the best options for you will be discussed.</p>
      </div>
    </section>
  </main>
  <p class="view-label">Inside</p>
</body>
</html>
```